Zielgruppe
Wir beraten Menschen aus unterschiedlichen Branchen, die im Rahmen Ihrer Tätigkeit vor einem technologischen Problem bzw. einer technologischen Lücke stehen und helfen diesen über vielfältige Bausteine, um so dem Unternehmen ein Unternehmensupgrade zu verschaffen. Wir schlagen somit eine Brücke zwischen dem Stand von heute in einem Unternehmen zu einem besseren Stand morgen.
Konkret betreiben wir unter anderem externes Projektmanagement, beschaffen Informationen unterschiedlicher Art, vermitteln Kooperationspartner, beraten individuell uvm.
Ob jemand nach einer neuen, innovativen Technologie sucht, Partner benötigt, um eigene Neuentwicklungen voranzutreiben, ein neues Produkt fürs eigene Unternehmen und einen entsprechenden Prototypen sucht, verwendete Stoffe mit anderen ersetzen will - mithilfe unseres weltweiten Expertennetzwerks von über 600.000 direkten Ansprechpartnern finden wir für die meisten Nöte dieser Art eine Lösung bzw. jemanden, der diese lösen kann.
Im Grunde genommen beseitigen wir Engpässe innerhalb von Industrieunternehmen, die beispielsweise sein können
-fehlende TEchnologien/Ersatzprodukte/Ersatzstoffe
-fehlende Ideen für Neuentwicklungen
-fehlendes Wissen im Unternehmen
-fehlende Objektivität hinsichtlich interner Verbesserungsmöglichkeiten
-fehlende Zeit für eigene Projekte, Neuentwicklungen und Suchen versch. Art
Wir finden
- neue Technologien, Ersatzprodukte, Ersatzstoffe
- Ideen für Neuentwicklungen und zusätzlich diejenigen, die dabei unterstützen können
- neue Märkte, um das Unternehmen zu erweitern
- das fehlende Wissen
- den nötigen Abstand, um interne Prozesse und Abläufe objektiv zu beurteilen und geben Vorschläge zur Veränderung/Verbesserung
- passende Realisierungspartner
Wie?
- wir recherchieren (Patente, Literatur) und sammeln Hintergrundwissen
- wir befragen unser Netzwerk und Unternehmen/Wissenschaftler
- wir setzen unsere Töchter..
Aufgabenstellung
Wir benötigen einen faltbaren Flyer, allerdings keinen klassischen, sondern wie ein Theatervorhang. Beispielbilder sind anbei (wir würden die Flyer drucken lassen und dann selbst falten). Wir gehen gerne andere Wege, auch in unseren Projekten.
Der Mensch und dessen Wünsche soll im Mittelpunkt stehen.
Design sollte nicht zu verspielt sein, sich daran orientieren, dass deutsche Unternehmen damit angesprochen werden.
Einen Beispielflyer mit den (noch variablen) Texten ist beigefügt, das Design muss sich nicht daran orientieren. Gute Alternativen sind mehr als gewünscht.
Der Gedanke hinter dem Flyer: Wir schlagen eine Brücke für den Kunden/Menschen zu seinem Ziel. Die Tools, die wir dazu nutzen sind Steine oder wir sprengen den Weg frei zum Ziel o.ä. Auch hier sind Alternativen mehr als willkommen.
Sie dürfen sich so weit wie möglich vom Beispielentwurf und dem Bild der Brücke zum Ziel lösen. Je kreativer und einleuchtender, desto besser. Gerne auch humorvoll, gerne einfach anders.

```html
<!DOCTYPE html>
<html lang="de">
<head>
<meta charset="utf-8">
<title>Faltflyer Unternehmensupgrade</title>
<link href="https://fonts.googleapis.com/css2?family=Roboto:wght@300;400;500;700&family=Roboto+Condensed:wght@300;400;700&display=swap" rel="stylesheet">
<style>
:root{
  --navy:#0c3f80;
  --navy-deep:#0a2a57;
  --navy-box:#0d2f5e;
  --curtain-light:#2a7fe6;
  --curtain-mid:#1656b8;
  --curtain-dark:#06204a;
  --white:#ffffff;
  --ink:#0c2f63;
  --orange:#f5a200;
  --faint:#e3e7ef;
  --page:#ffffff;
}
*{box-sizing:border-box;margin:0;padding:0}
html,body{width:1200px;height:2400px;overflow:hidden;background:var(--page)}
body{position:relative;font-family:"Roboto",Arial,sans-serif;color:var(--white)}
.panel{position:absolute;overflow:hidden}
.curtain{
  background:
    radial-gradient(ellipse 90% 35% at 50% 10%, rgba(110,180,255,.45), rgba(110,180,255,0) 70%),
    linear-gradient(180deg, var(--curtain-light) 0%, var(--curtain-mid) 50%, var(--curtain-dark) 100%);
}
.curtain-seam{position:absolute;top:0;bottom:0;width:2px;background:#02122e}
.kicker{font-family:"Roboto Condensed",Arial,sans-serif;font-weight:300;letter-spacing:.06em;font-size:12px}
.welcome{font-family:"Roboto Condensed",Arial,sans-serif;font-weight:300;font-size:12px;line-height:1.3}
.welcome strong{font-family:"Roboto",Arial,sans-serif;font-weight:700;display:block}
.brand{position:absolute;display:flex;align-items:center;gap:8px;font-family:"Roboto",Arial,sans-serif;font-weight:400;font-size:22px;color:var(--white)}
.brand-dot{width:26px;height:26px;border-radius:50%;background:var(--white)}

/* closed front */
.closed{left:439px;top:105px;width:330px;height:598px}

/* inside spread */
.inside-left{left:111px;top:736px;width:168px;height:603px}
.inside-center{left:279px;top:740px;width:623px;height:599px;background:linear-gradient(180deg,var(--navy) 0%,var(--navy) 55%,var(--navy-deep) 100%)}
.inside-right{left:902px;top:736px;width:165px;height:603px}
.network-visual{position:absolute;left:0;right:0;top:340px;bottom:0;background:radial-gradient(ellipse 70% 60% at 35% 100%, #3f8fe0 0%, #13498f 45%, rgba(10,42,87,0) 80%)}
.title{position:absolute;left:36px;top:36px;font-size:32px;font-weight:500;line-height:1.1}
.expect{position:absolute;left:36px;top:172px;width:160px}
.expect h3{font-size:8px;font-weight:400;letter-spacing:.06em;margin-bottom:6px}
.expect li{list-style:none;font-family:"Roboto Condensed",Arial,sans-serif;font-weight:700;font-size:12.5px;line-height:1.35;margin-bottom:7px}
.roles{position:absolute;left:232px;top:134px;width:244px;height:136px;background:var(--navy-box);padding:12px 13px}
.roles h4{font-size:8px;font-weight:400;letter-spacing:.05em;color:var(--orange);margin-bottom:4px}
.roles p{font-size:14px;font-weight:300;line-height:1.2;margin-bottom:16px}
.message{position:absolute;left:188px;top:270px;width:244px;height:258px;background:var(--white);color:var(--ink);padding:10px 9px;font-size:7.3px;line-height:1.38}
.message p{margin-bottom:8px}
.cta{position:absolute;left:177px;top:477px;width:126px;height:27px;background:var(--orange);color:var(--white);font-size:7.3px;font-weight:700;padding:4px 20px 0 19px;line-height:1.3}
.cta-phone{position:absolute;left:197px;top:510px;font-size:7.5px;color:var(--ink);font-weight:500}
.network-side{position:absolute;left:496px;top:44px;width:122px;font-size:7.5px;line-height:1.4}
.network-side h4{font-weight:400;letter-spacing:.06em;font-size:8px;margin-bottom:4px}
.network-side p{margin-bottom:10px}
.network-side .call{font-size:10px;font-weight:500;line-height:1.3}
.claim{position:absolute;left:0;right:0;top:583px;text-align:center;font-size:8.5px;letter-spacing:.08em;padding-left:16px}

/* back */
.back-left{left:111px;top:1477px;width:164px;height:604px}
.back-right{left:903px;top:1477px;width:164px;height:604px}
.back-white{top:1477px;width:164px;height:604px;background:var(--white);color:var(--ink)}
.back-industry{left:275px}
.back-research{left:739px}
.back-center{left:439px;top:1477px;width:300px;height:604px;background:var(--navy)}
.ghost-word{position:absolute;left:50%;top:50%;transform:translate(-50%,-50%) rotate(-90deg);font-size:96px;font-weight:400;color:var(--faint);letter-spacing:.1em;white-space:nowrap;line-height:1}
.service-head{position:absolute;left:0;right:0;top:160px;text-align:center;font-size:10px;letter-spacing:.08em;line-height:1.15;font-weight:400}
.service-head strong{font-weight:700}
.service-list{position:absolute;left:8px;top:222px;width:135px;list-style:none}
.service-list li{position:relative;padding-left:6px;font-family:"Roboto Condensed",Arial,sans-serif;font-weight:700;font-size:7.5px;line-height:1.35;margin-bottom:10px;letter-spacing:.03em}
.service-list li::before{content:"";position:absolute;left:0;top:4px;width:2px;height:2px;background:var(--orange)}
.back-research .service-list{left:18px;width:120px}
.offer{position:absolute;left:38px;top:34px;width:230px}
.offer h2{font-family:"Roboto Condensed",Arial,sans-serif;font-weight:700;font-size:14px;line-height:1.45}
.rule{width:94px;height:2px;background:var(--orange);margin:18px 0 24px}
.offer p{font-size:9.6px;line-height:1.38;font-weight:300;margin-bottom:10px}
.offer .question{font-weight:500;font-size:10px;margin-top:24px}
.imprint{position:absolute;left:0;right:0;top:505px;text-align:center;font-size:7.5px;line-height:1.35}
.imprint strong{display:block;font-weight:700;margin-bottom:8px}
</style>
</head>
<body>

<!-- closed front -->
<section class="panel curtain closed" role="img" aria-label="Foto eines blauen Theatervorhangs mit Lichtkegel, geschlossen">
  <div class="curtain-seam" style="left:164px"></div>
  <p class="kicker" style="position:absolute;left:23px;top:30px">Vorhang auf!</p>
  <p class="welcome" style="position:absolute;left:23px;top:172px;width:140px">Wir begrüßen Sie herzlich zur Vorstellung:<strong>Unternehmensupgrade durch technologische Beratung</strong></p>
  <div class="brand" style="left:200px;top:532px"><span class="brand-dot"></span>nts</div>
</section>

<!-- inside spread -->
<section class="panel curtain inside-left" role="img" aria-label="Foto der linken Vorhanghälfte">
  <p class="kicker" style="position:absolute;left:23px;top:30px">Vorhang auf!</p>
  <p class="welcome" style="position:absolute;left:23px;top:172px;width:135px">Wir begrüßen Sie herzlich zur Vorstellung:<strong>Unternehmensupgrade durch technologische Beratung</strong></p>
</section>

<section class="panel inside-center">
  <div class="network-visual" role="img" aria-label="Erdkugel mit leuchtendem Netzwerk aus verbundenen Punkten"></div>
  <h1 class="title">Unternehmensupgrade<br>durch technologische<br>Beratung</h1>
  <div class="expect">
    <h3>SIE DÜRFEN ERWARTEN:</h3>
    <ul>
      <li>… Verbesserungen</li>
      <li>… Veränderungen</li>
      <li>… Übernahme von<br>&nbsp;&nbsp;&nbsp;Projekten oder<br>&nbsp;&nbsp;&nbsp;Teilaufgaben</li>
      <li>… Innovationen</li>
      <li>… Beseitigung von<br>&nbsp;&nbsp;&nbsp;Störfaktoren</li>
      <li>… Dokumentation des<br>&nbsp;&nbsp;&nbsp;Vorgehens</li>
    </ul>
  </div>
  <div class="roles">
    <h4>IN DER HAUPTROLLE:</h4>
    <p>Ihr Unternehmen</p>
    <h4>IN DER NEBENROLLE:</h4>
    <p style="font-size:12.5px">nts als Gesamtprojektleitung<br>in Form eines Generalunternehmers</p>
  </div>
  <div class="message">
    <p>Sie investieren viel kostbare Zeit und Geld in ein neues Entwicklungsprojekt, haben aber nicht recherchiert, ob es dafür überhaupt <strong>Interessenten auf dem Markt</strong> gibt. Am Ende stellen Sie fest, dass aufgrund von schlechten Annahmen und mangelnder Information das Projektergebnis wertlos und das Geld in den Sand gesetzt ist.</p>
    <p>Sie haben keine Zeit oder Lust, sich um <strong>Innovationen in Ihrem Bereich</strong> zu kümmern oder diese weiter voranzutreiben. Die Auftragsbücher sind (noch) voll, <strong>das Tagesgeschäft nimmt überhand</strong>, es mangelt an Personal – alles verständliche Argumente gegen Innovationen.</p>
    <p>Mit unserem individuellen Projektmanagement kümmern wir uns individuell um Ihr Anliegen, egal ob Forschung oder Industrie. Bei Bedarf erweitern wir unser kreatives Expertenteam um weitere „Nebendarsteller“ aus unserem globalen Netzwerk.</p>
  </div>
  <div class="cta">Rufen Sie uns an für eine kostenlose Beratung:</div>
  <p class="cta-phone">+49 (0)555 310 42 0</p>
  <div class="network-side">
    <h4>EXPERTENNETZWERK:</h4>
    <p>Sie als Unternehmen oder Institut in der Forschung haben ein neues Verfahren entwickelt und suchen nun einen geeigneten Entwicklungs-/Anwendungspartner?</p>
    <p><strong>Nutzen Sie unser einzigartiges nts-Expertennetzwerk.</strong><br>Wir finden für Sie industrielle Kooperationspartner, Lizenznehmer, Patentkäufer oder Partner zur Beantragung von Fördermitteln.</p>
    <p>Sie nennen mir Ihre Ziele und Wünsche, gemeinsam definieren wir unser Projekt!</p>
    <p class="call">Rufen Sie jetzt an:<br>+49 555 310 42 13</p>
  </div>
  <p class="claim">INNOVATION. INFORMATION. KOOPERATION.</p>
</section>

<section class="panel curtain inside-right" role="img" aria-label="Foto der rechten Vorhanghälfte">
  <div class="brand" style="left:30px;top:540px"><span class="brand-dot"></span>nts</div>
</section>

<!-- back -->
<section class="panel curtain back-left" role="img" aria-label="Foto der linken Vorhanghälfte, Rückseite"></section>

<section class="panel back-white back-industry">
  <span class="ghost-word" aria-hidden="true">INDUSTRIE</span>
  <h3 class="service-head">WIR SIND IHR<br><strong>INFORMATIONS-<br>DIENSTLEISTER</strong> FÜR<br>BEISPIELSWEISE:</h3>
  <ul class="service-list">
    <li>Marktanalysen, Wettbewerbsanalysen und Markteinführung</li>
    <li>Wissensmanagement und nachhaltigen Knowledge-Transfer</li>
    <li>Innovationsmanagement und Innovationsstrategie</li>
    <li>Produktinnovation und Produktentwicklung</li>
    <li>Zukunftstrends- und Ideenmanagement</li>
    <li>Lieferanten, Experten, Messen</li>
  </ul>
</section>

<section class="panel back-center">
  <div class="offer">
    <h2>NTS liefern Ihnen maßgeschneiderte, individuelle Lösungen für Ihr Projekt.</h2>
    <div class="rule"></div>
    <p>Sie sagen, was Sie benötigen –<br>wir kümmern uns um die Lösung.</p>
    <p>Im Bereich der Forschung vermitteln wir Projektpartner, für die Industrie beschaffen wir Informationen, Lösungen und Experten.</p>
    <p>Wenn Sie NTS beauftragen, bekommen Sie ein heterogenes Team mit kreativen Köpfen an Ihrer Seite, die sich um Ihr Anliegen kümmern. Je nach Anforderungen können wir uns aus einem globalen Netzwerk an „Nebenakteuren“ aus jedem Technologiebereich bedienen.</p>
    <p class="question">Wann drehen wir Ihre Erfolgsstory?</p>
  </div>
  <div class="brand" style="left:120px;top:450px;font-size:17px;gap:6px"><span class="brand-dot" style="width:20px;height:20px"></span>nts</div>
  <div class="imprint">
    <strong>Norder Technikservice GmbH</strong>
    Tel: +49 (0)555 310420<br>Lindenweg 14<br>D-12345 Musterstadt<br>www.technikservice-beispiel.de
  </div>
</section>

<section class="panel back-white back-research">
  <span class="ghost-word" aria-hidden="true">FORSCHUNG</span>
  <h3 class="service-head">WIR SIND IHR<br><strong>ANSPRECHPARTNER</strong><br>FÜR:</h3>
  <ul class="service-list">
    <li>Wissens- und Technologietransfer</li>
    <li>Lizenznehmer und Partner aus der Industrie</li>
    <li>Technologieberatung</li>
    <li>Technologie- und Innovationsmanagement</li>
    <li>Optimierung der Produktentwicklungsprozesse</li>
    <li>Industriepartner für Verbundprojekte</li>
    <li>Patentverwertung</li>
    <li>Markteintritt</li>
  </ul>
</section>

<section class="panel curtain back-right" role="img" aria-label="Foto der rechten Vorhanghälfte, Rückseite"></section>

</body>
</html>
```